Lorna Vee Tresses Fancy Business Card’s

I want my business cards to be elite, original and very classy. I want the business cards to match the colors of my logo and to match the design posted. I would love the design of the picture I posted

I want the card all white .
The dripping on the top of the card I want it to match the pink color in my logo that’s also posted .
I need my logo on the business card !
I need my Instagram- @lorna.vee.tresses__
And my phone number - 555 207 9362

Target Market(s)

My target market is young woman age 23 to older woman to the age of 65
I want both older and younger women to love my design . I don’t want any cheap looking business cards

Industry/Entity Type

Hair And Beauty

Contact Information for Business Card

Add my logo
Add my Instagram- @lorna.vee.tresses__
My number - 555 207 9362
My website- www.lornaveetresses-example.com

Font styles to use
Serif
Script

Colors
ffffff
e667a6
e34298

Requirements
Must have
• The business cards must have my logo, my number , my website, and my Instagram!
Nice to have
• Nice to have glitter words that match my logo
• The business cards must look classy and mature
• I want them to be very unique!!
Should not have
• Should not have any colors that doesn’t match my logo ! This is very important! Please

```html
<!DOCTYPE html>
<html lang="en">
<head>
<meta charset="utf-8">
<title>Lorna Vee Tresses — Business Card</title>
<link rel="stylesheet" href="https://fonts.googleapis.com/css2?family=Playfair+Display:wght@400&family=Montserrat:wght@400;500&display=swap">
<style>
  :root {
    --pink: #e34298;
    --pink-soft: #e667a6;
    --white: #ffffff;
    --stage: #ececef;
    --shadow: rgba(60, 20, 45, 0.18);
  }
  * { box-sizing: border-box; margin: 0; padding: 0; }
  html, body { width: 1200px; height: 900px; overflow: hidden; }
  body {
    background: var(--stage);
    display: flex;
    flex-direction: column;
    align-items: center;
    justify-content: center;
    gap: 40px;
    font-family: "Montserrat", sans-serif;
  }
  .card {
    position: relative;
    width: 700px;
    height: 400px;
    border-radius: 4px;
    overflow: hidden;
    box-shadow: 0 10px 30px var(--shadow);
  }
  .card-front { background: var(--white); }
  .card-back { background: var(--pink); display: flex; align-items: center; justify-content: center; }

  .front-swoosh { position: absolute; inset: 0; width: 100%; height: 100%; }

  .brand-name {
    font-family: "Playfair Display", serif;
    font-weight: 400;
    text-align: center;
    line-height: 1.05;
  }
  .card-front .brand-name {
    position: absolute;
    top: 70px;
    left: 250px;
    width: 340px;
    font-size: 54px;
    color: var(--pink);
  }
  .card-back .brand-name {
    font-size: 70px;
    color: var(--white);
    width: 460px;
  }

  .contact-row {
    position: absolute;
    left: 28px;
    bottom: 26px;
    display: flex;
    align-items: center;
    gap: 14px;
    color: var(--white);
    font-size: 12.5px;
    font-weight: 500;
    letter-spacing: 0.3px;
  }
  .contact-item { display: flex; align-items: center; gap: 6px; }
  .contact-divider { width: 1px; height: 14px; background: rgba(255,255,255,0.7); }
  .contact-icon { width: 13px; height: 13px; flex: none; }
</style>
</head>
<body>

  <section class="card card-front" aria-label="Business card front">
    <svg class="front-swoosh" viewBox="0 0 700 400" preserveAspectRatio="none" aria-hidden="true">
      <path d="M0 150 C 90 290, 330 350, 700 370 L 700 400 L 0 400 Z" fill="var(--pink)"/>
      <path d="M0 128 C 95 275, 335 334, 700 352" fill="none" stroke="var(--pink)" stroke-width="3"/>
    </svg>

    <h1 class="brand-name">Lorna Vee Tresses</h1>

    <div class="contact-row">
      <span class="contact-item">
        <svg class="contact-icon" viewBox="0 0 24 24" aria-hidden="true">
          <path fill="var(--white)" d="M6.6 10.8a15.1 15.1 0 0 0 6.6 6.6l2.2-2.2a1 1 0 0 1 1-.25 11.4 11.4 0 0 0 3.6.57 1 1 0 0 1 1 1V20a1 1 0 0 1-1 1A17 17 0 0 1 3 4a1 1 0 0 1 1-1h3.5a1 1 0 0 1 1 1c0 1.25.2 2.45.57 3.57a1 1 0 0 1-.25 1z"/>
        </svg>
        555 207 9362
      </span>
      <span class="contact-divider"></span>
      <span class="contact-item">
        <svg class="contact-icon" viewBox="0 0 24 24" aria-hidden="true">
          <circle cx="12" cy="12" r="9" fill="none" stroke="var(--white)" stroke-width="2"/>
        </svg>
        @lorna.vee.tresses__
      </span>
      <span class="contact-divider"></span>
      <span class="contact-item">
        <svg class="contact-icon" viewBox="0 0 24 24" aria-hidden="true">
          <circle cx="12" cy="12" r="9" fill="none" stroke="var(--white)" stroke-width="2"/>
          <ellipse cx="12" cy="12" rx="4" ry="9" fill="none" stroke="var(--white)" stroke-width="1.6"/>
          <line x1="3" y1="12" x2="21" y2="12" stroke="var(--white)" stroke-width="1.6"/>
        </svg>
        www.lornaveetresses-example.com
      </span>
    </div>
  </section>

  <section class="card card-back" aria-label="Business card back">
    <h2 class="brand-name">Lorna Vee Tresses</h2>
  </section>

</body>
</html>
```